This will be a design for publicity materials for an event:

DEBATE: That the NMC will harm Asia's growing digital economies

Date: 18 July 2013, 19:00-21:00
Venue: Function Room 6, Level 3, The Orchid Valehouse, Kota Kinabalu, Malaysia
RSVP: to marcus@velbrinex.org by 11 July 2013, limited free tickets available

- blurb begins -

The Northern Meridian Compact offers a golden opportunity for Asian nations to reap the rich rewards of global trade - or else it poses a dire threat to their sovereignty that would allow foreign multinational corporations to rewrite national laws for their own benefit. Opinions about the merits of the Northern Meridian Compact for Asia are polarised, making it difficult for ordinary citizens to separate fact from fiction. So what better topic for a debate, to clear the air and shed some light on this impenetrable and controversial subject?

Patron Guild Worldwide, in partnership with Byteline Report Hub, is hosting a free public 3-on-3 parliamentary-style debate on the proposition "That the NMC will harm Asia's growing digital economies". Drawn from across the region's government, industry and NGO communities, the participants will attempt to convince the audience that the NMC is the best hope for stimulating growth and innovation in Asia's high-tech industries - or that it will hamstring those industries with inappropriate laws pushed by foreign interests. Who wins? The audience will decide.

- blurb ends -

We want to have a design in 4 formats to promote this online, but you can just do one format to respond to the brief, and the others can come after I select a winner. One of the formats should be suitable to be emailed, so you could do it either as a graphic, or else as an HTML page suitable for emailing. The second format should be a 430 x 130 banner. Third should be a 300 x 250 banner. Also one format in about 800x600 or similar that we can use as a presentation slide at the venue.

Just to clarify, you don't need to include the whole blurb text.  Particularly in the small formats, that would be impossible.  It is mainly included as background for you.

I apologise for not getting back to you with comments and feedback - I had to travel to India and don't have proper Internet access here. I will get back to you as soon as I can. 

Target Market(s)

Business people, NGOs, diplomats

Industry/Entity Type

Industry

Requirements
Must have
• Sponsors' logos are attached.
Nice to have
• In at least the larger formats, we need to have space to show the names of the debaters. But we don't have those names yet, so for now it should say something like "Debating teams announced soon", with the facility to change it later when we do have the names. I had thought about maybe using a stage with a curtain drawn for the "coming soon" variant, and the curtains drawn back to reveal the names for the final variant. But I leave this to you.
Should not have
• Prefer if you don't use stock photos of people.

```html
<!DOCTYPE html>
<html lang="en">
<head>
<meta charset="utf-8">
<title>Debate: That the NMC will harm Asia's growing digital economies</title>
<link href="https://fonts.googleapis.com/css2?family=Open+Sans:ital,wght@0,300;0,400;0,700;1,400;1,600&family=Patrick+Hand&display=swap" rel="stylesheet">
<style>
  :root {
    --navy-deep: #0b1a3d;
    --navy: #1c3a78;
    --sky: #7fb4dc;
    --sky-pale: #cfe4f2;
    --yellow: #ffe21a;
    --amber: #f5a000;
    --ink: #0f2350;
    --white: #ffffff;
    --logo-ink: #1b3b7a;
  }
  html, body {
    margin: 0;
    padding: 0;
    overflow: hidden;
    background: #e8eef4;
  }
  .poster {
    position: relative;
    width: 1200px;
    height: 900px;
    overflow: hidden;
    font-family: "Open Sans", Arial, sans-serif;
    background: linear-gradient(180deg, var(--navy-deep) 0%, var(--navy) 22%, #3a6fae 42%, var(--sky) 58%, var(--sky-pale) 78%, #eef6fb 100%);
  }
  .kicker {
    position: absolute;
    top: 14px;
    left: 0;
    width: 100%;
    margin: 0;
    text-align: center;
    font-size: 38px;
    font-weight: 700;
    color: var(--yellow);
    letter-spacing: 0.5px;
  }
  .motion {
    position: absolute;
    top: 66px;
    left: 0;
    width: 100%;
    margin: 0;
    text-align: center;
    font-size: 46px;
    font-weight: 300;
    color: var(--white);
    letter-spacing: 0.2px;
  }
  .bulbs-art {
    position: absolute;
    top: 145px;
    left: 0;
    width: 1200px;
    height: 270px;
    background:
      radial-gradient(ellipse 90px 110px at 17% 45%, rgba(255,240,120,0.55), transparent 70%),
      radial-gradient(ellipse 90px 110px at 33% 45%, rgba(240,90,200,0.55), transparent 70%),
      radial-gradient(ellipse 90px 110px at 50% 45%, rgba(60,200,255,0.6), transparent 70%),
      radial-gradient(ellipse 90px 110px at 67% 45%, rgba(170,100,220,0.55), transparent 70%),
      radial-gradient(ellipse 90px 110px at 83% 45%, rgba(90,220,110,0.55), transparent 70%);
  }
  .blurb {
    position: absolute;
    top: 440px;
    left: 52px;
    width: 1110px;
    margin: 0;
    font-size: 25px;
    line-height: 36px;
    font-style: italic;
    font-weight: 600;
    color: var(--ink);
  }
  .blurb .name {
    color: var(--white);
    font-size: 30px;
    font-weight: 400;
  }
  .teams-arrow {
    position: absolute;
    top: 575px;
    left: 0;
    width: 660px;
    height: 150px;
  }
  .teams-label {
    position: absolute;
    top: 622px;
    left: 52px;
    margin: 0;
    font-size: 33px;
    font-weight: 400;
    color: #111;
  }
  .globe-art {
    position: absolute;
    top: 560px;
    left: 555px;
    width: 645px;
    height: 340px;
    background: radial-gradient(ellipse 520px 330px at 75% 115%, #2a64b0 0%, #4d8fd0 45%, rgba(160,205,235,0.6) 70%, transparent 85%);
  }
  .details {
    position: absolute;
    top: 715px;
    right: 18px;
    width: 390px;
    margin: 0;
    text-align: right;
    font-size: 16px;
    line-height: 22px;
    color: var(--white);
    text-shadow: 0 1px 3px rgba(0,0,0,0.8);
  }
  .details b { font-weight: 700; }
  .details .tickets {
    display: block;
    margin-top: 6px;
    font-family: "Patrick Hand", cursive;
    font-size: 21px;
  }
  .sponsors {
    position: absolute;
    left: 22px;
    bottom: 28px;
    display: flex;
    align-items: center;
    gap: 34px;
  }
  .sponsor {
    display: flex;
    align-items: center;
    gap: 8px;
    font-size: 17px;
    font-weight: 700;
    color: var(--logo-ink);
    line-height: 20px;
  }
  .sponsor .mark {
    width: 22px;
    height: 22px;
    background: var(--logo-ink);
    flex: none;
  }
  .sponsor .mark.round { border-radius: 50%; }
</style>
</head>
<body>
  <main class="poster">
    <h1 class="kicker">DEBATE</h1>
    <h2 class="motion">That the NMC will harm Asia's growing digital economies</h2>

    <div class="bulbs-art" role="img" aria-label="Row of five glowing light bulbs in yellow, pink, blue, purple and green"></div>

    <p class="blurb">The <span class="name">Northern Meridian Compact</span> offers a golden opportunity for Asian nations to reap the rich rewards of global trade. <span class="name">NMC</span> is the best hope for stimulating growth and innovation in Asia's high-tech industries</p>

    <svg class="teams-arrow" viewBox="0 0 660 150" aria-hidden="true">
      <defs>
        <linearGradient id="arrowFill" x1="0" y1="0" x2="1" y2="0">
          <stop offset="0" stop-color="#ffe21a"/>
          <stop offset="0.7" stop-color="#ffd21a"/>
          <stop offset="1" stop-color="#f5a000"/>
        </linearGradient>
      </defs>
      <polygon points="0,43 560,43 560,3 648,75 560,147 560,97 0,97" fill="url(#arrowFill)"/>
    </svg>
    <p class="teams-label">Debating teams announced soon</p>

    <div class="globe-art" role="img" aria-label="Silhouetted business people walking across the curve of a blue globe"></div>

    <p class="details">
      <b>Date:</b> 18 July 2013, 19:00-21:00<br>
      <b>Venue:</b> Function Room 6, Level 3,<br>
      The Orchid Valehouse, Kota Kinabalu, Malaysia<br>
      <b>RSVP:</b> to marcus@velbrinex.org by 11 July 2013
      <span class="tickets">limited free tickets available</span>
    </p>

    <footer class="sponsors">
      <div class="sponsor"><span class="mark"></span>Even Terms</div>
      <div class="sponsor"><span class="mark round"></span>Byteline Report Hub</div>
      <div class="sponsor"><span class="mark round"></span>Patron Guild Worldwide</div>
    </footer>
  </main>
</body>
</html>
```